QZN Supplements needs a label designer for supplement company

Looking for an on going label designer for my supplement company. I have three products that will need designs. I'm about to launch my sleep supplement called Velmora Rest and that's the first design needed.
I would like all designs to be somewhat simple, not overstated and uniformed so that when you look at all of the labels of the different supplements they are similar and you can tell it's the same brand.
Please see attached sample pictures below as ideas.
Updates

The brand is QZN supplements, logo file has been provided. The supplement is called Velmora Rest. It is a liquid supplement that is a 32/33 ounce white bottle. Die lines and measurements will be provided. Here's text for wording ideas: Wording: Natural Sleep Aid Reset your circadian rhythm. May help you: Fall asleep faster. Get a deeper more restful sleep. Boost Immune System Remember your dreams. Protect your brain and flush toxins. Wake up feeling refreshed. Non-gmo Gluten Free Sugar Free Vegan Manufactured in cGMP factory Manufactured in USA

Target Market(s)

Health and wellness/supplement industry for regular people not hardcore gym goers. My supplements are for a health lifestyle not bodybuilding.

Industry/Entity Type

Health And Wellness

Colors
3176b5
3276b5
33a6d7
85cae6
85abd2
cedeed
e4daeb
b7a5cd

Requirements
Must have
• There will be some text and wording that I will provide that must be on the bottles.

```html
<!DOCTYPE html>
<html lang="en">
<head>
<meta charset="utf-8">
<title>Velmora Rest – QZN Supplements Label</title>
<link rel="stylesheet" href="https://fonts.googleapis.com/css2?family=Exo+2:wght@400;600&display=swap">
<style>
  :root {
    --page-bg: #e6f0f4;
    --label-deep: #2a1fbf;
    --label-mid: #3d36b0;
    --label-violet: #4a3aa8;
    --text-light: #f4f4fb;
    --glow-cyan: #33c9e8;
    --glow-blue: #1d5fd6;
    --rule: #e8e8f5;
  }
  * { margin: 0; padding: 0; box-sizing: border-box; }
  html, body {
    width: 1200px;
    height: 960px;
    overflow: hidden;
    background: var(--page-bg);
    font-family: "Exo 2", sans-serif;
  }
  .label {
    position: absolute;
    left: 300px;
    top: 60px;
    width: 600px;
    height: 840px;
    background: linear-gradient(120deg, var(--label-violet) 0%, var(--label-mid) 40%, var(--label-deep) 100%);
    color: var(--text-light);
    overflow: hidden;
  }
  .brand {
    position: absolute;
    top: 88px;
    left: 90px;
    display: flex;
    align-items: center;
    gap: 14px;
  }
  .brand-dot {
    width: 50px;
    height: 50px;
    border-radius: 50%;
    background: var(--text-light);
  }
  .brand-name {
    font-weight: 600;
    font-size: 36px;
    letter-spacing: 0.5px;
    text-transform: uppercase;
    color: var(--text-light);
  }
  .product-name {
    position: absolute;
    top: 240px;
    left: 0;
    width: 100%;
    text-align: center;
    font-weight: 400;
    font-size: 88px;
    letter-spacing: 1px;
  }
  .tagline-block {
    position: absolute;
    top: 415px;
    left: 50px;
    padding-left: 14px;
    border-left: 2px solid var(--rule);
  }
  .tagline {
    font-size: 33px;
    line-height: 42px;
    letter-spacing: 1px;
  }
  .claims {
    margin-top: 20px;
    font-size: 22px;
    letter-spacing: 0.5px;
  }
  .wave-art {
    position: absolute;
    left: 0;
    top: 560px;
    width: 100%;
    height: 200px;
    background:
      radial-gradient(ellipse 55% 40% at 30% 55%, rgba(51,201,232,0.85), rgba(51,201,232,0) 70%),
      radial-gradient(ellipse 60% 45% at 75% 60%, rgba(51,201,232,0.6), rgba(51,201,232,0) 70%),
      linear-gradient(180deg, rgba(29,95,214,0) 0%, var(--glow-blue) 50%, rgba(29,95,214,0) 100%);
  }
  .volume {
    position: absolute;
    top: 742px;
    left: 0;
    width: 100%;
    text-align: center;
    font-size: 27px;
    letter-spacing: 1px;
  }
</style>
</head>
<body>
  <main class="label">
    <div class="brand">
      <span class="brand-dot"></span>
      <span class="brand-name">QZN Supplements</span>
    </div>
    <h1 class="product-name">Velmora Rest</h1>
    <div class="tagline-block">
      <p class="tagline">Natural sleep aid to reset<br>your circadian rhythm</p>
      <p class="claims">Non-GMO · Vegan · Sugar Free</p>
    </div>
    <div class="wave-art" role="img" aria-label="Glowing cyan particle wave across the lower label"></div>
    <p class="volume">32 fl oz Liquid</p>
  </main>
</body>
</html>
```